Powerpoint Design for AI Consulting Company

Description
Harbor Quill Industries is a consulting and technology company that engineers AI transformations, automation, and decision intelligence for financial firms, mining companies, and supply chains.
We already have a logo and brand colors (see attached). We need a professional, modern PowerPoint template that reflects our brand identity and positioning.
Key Requirements
Use our logo and color palette (deep blue, orange, white/black backgrounds).
Clean, modern design with subtle technology-inspired elements (data flows, AI networks, abstract systems).
Must feel sophisticated, bold, and boardroom-ready for executive presentations.
Templates should support both dark and light backgrounds.
Deliverables
A reusable PowerPoint template (.PPTX) with at least these layouts:
Title / Cover slide – dramatic, logo placement, tagline space.
Agenda slide – clean, structured layout.
Section divider slides – strong use of brand colors.
Content slides – text + image, text + icon.
Charts & data slides – bar, line, pie, comparison table, infographics.
Case study / example project slide. - ROI / Transformation Journey
Timeline / roadmap slide.
Team profile slide.
Reframe Slide – A provocative insight that reframes the client’s current thinking.
Options & Trade-offs Slide – Matrix showing different paths and consequences.
Execution Roadmap Slide – Step-by-step phased implementation view.
Closing / thank-you slide with contact details.
Style Guide
Colors: Primary – deep blue (#0D3559), Secondary – orange (#E87722), Accents – silver/white.
Fonts: Modern sans-serif (e.g., Montserrat, Lato, or similar).
Visual elements: Abstract technology, data-inspired graphics, mathematical motifs. Avoid clutter or overly “sci-fi” looks.
Tone: Premium consulting + innovative AI firm.
Target Market(s)
Harbor Quill Industries’ target market is senior decision-makers in finance, mining, and supply chains, where complexity, risk, and ROI pressure are high. Primary buyers include family offices, boutique wealth managers, super funds, and mining/supply chain executives, who value insight-driven strategies, automation, and decision intelligence. A secondary market includes professional services (accounting, legal, medical) and regulated SMEs (daycare, aged care, community services) burdened by admin and compliance. The slide deck must appeal to a boardroom audience — authoritative, data-driven, and visually clean — while remaining flexible enough to adapt for SME professional services.
Look and feel
Each slider illustrates characteristics of the customer's brand and the style your logo design should communicate.

```html
<!DOCTYPE html>
<html lang="en">
<head>
<meta charset="utf-8">
<title>Harbor Quill Industries – Presentation Template</title>
<link href="https://fonts.googleapis.com/css2?family=Montserrat:wght@400;600;700;800;900&family=Lato:wght@400;700&display=swap" rel="stylesheet">
<style>
:root{
  --navy:#163a62;
  --navy-deep:#0d3559;
  --orange:#e87722;
  --white:#ffffff;
  --silver:#c9cfe6;
  --ink:#1d2b44;
  --soft:#dfe4ef;
}
*{box-sizing:border-box;margin:0;padding:0}
html,body{width:1200px;height:2259px;overflow:hidden;background:#fff}
body{position:relative;font-family:"Lato",sans-serif;color:var(--white)}
.slide{position:absolute;width:466px;height:262px;overflow:hidden;
  background:radial-gradient(ellipse 70% 60% at 100% 100%,rgba(232,119,34,.95) 0%,rgba(232,119,34,.45) 30%,rgba(22,58,98,0) 70%),var(--navy)}
.slide.plain{background:var(--navy)}
.col-l{left:131px}.col-r{left:606px}
.r1{top:126px}.r2{top:415px}.r3{top:704px}.r4{top:993px}.r5{top:1282px}.r6{top:1571px}.r7{top:1860px}
.footer-line{position:absolute;left:0;right:0;bottom:14px;height:1px;background:rgba(255,255,255,.35)}
.page-no{position:absolute;right:54px;bottom:9px;width:32px;height:10px;border:1px solid rgba(255,255,255,.6);border-radius:3px;background:var(--orange);font:700 5px "Montserrat",sans-serif;text-align:center;line-height:8px;color:var(--navy)}
.brand-tag{position:absolute;right:12px;top:18px;width:64px;height:32px;background:#fff;border-radius:2px;display:flex;align-items:center;justify-content:center;gap:3px;padding:0 4px}
.brand-tag i{width:5px;height:5px;border-radius:50%;background:var(--navy-deep);flex:none}
.brand-tag span{font:700 5px/1.15 "Montserrat",sans-serif;color:var(--navy-deep);text-transform:uppercase}
.title{position:absolute;font:800 15px "Montserrat",sans-serif;color:#fff;letter-spacing:.2px}
.title em{font-style:normal;color:var(--orange)}
.body{font-size:5.2px;line-height:1.45;color:#e8ecf5;text-align:justify}
.photo{position:absolute;background:linear-gradient(150deg,#d9dde4,#8f9aab 60%,#4d5a70)}
/* cover */
.cover-card{position:absolute;left:118px;top:72px;width:232px;height:118px;background:#fff;border:4px solid var(--silver);border-radius:5px;display:flex;flex-direction:column;align-items:center;justify-content:center;gap:10px}
.cover-name{display:flex;align-items:center;gap:6px}
.cover-name i{width:12px;height:12px;border-radius:50%;background:var(--navy-deep)}
.cover-name span{font:800 13px "Montserrat",sans-serif;color:var(--navy-deep);text-transform:uppercase;letter-spacing:.3px}
.cover-thanks{font:900 19px "Montserrat",sans-serif;color:var(--orange);letter-spacing:.5px}
/* agenda */
.agenda-item{position:absolute;left:20px;width:211px;height:20px;background:#f1f2f6;border-radius:3px;font:800 8px/20px "Montserrat",sans-serif;color:var(--orange);padding-left:11px}
/* section divider */
.ring{position:absolute}
.side-text{position:absolute;width:135px}
.side-text.orange{color:var(--orange)}
/* about */
.check-row{position:absolute;display:flex;gap:3px;width:100px;font-size:5px;line-height:1.35;color:#e8ecf5}
.check-row b{color:var(--orange);font-size:9px;line-height:8px}
/* how */
.how-circle{position:absolute;width:104px;height:104px;border-radius:50%;background:#fff;border:3px solid var(--orange);display:flex;flex-direction:column;align-items:center;justify-content:center;color:var(--ink)}
.how-circle h4{font:700 8px "Montserrat",sans-serif;margin-top:4px}
.how-circle ul{list-style:none;font-size:5px;margin-top:3px}
.how-circle li::before{content:"● ";color:#9a7a2a}
/* case study */
.case-item{position:absolute;left:207px;display:flex;gap:9px;align-items:center}
.case-icon{width:34px;height:34px;border-radius:50%;background:#fff;border:2px solid rgba(255,255,255,.5);box-shadow:0 0 0 2px var(--navy);display:flex;align-items:center;justify-content:center;flex:none}
.case-item h5{font:700 6px "Montserrat",sans-serif;color:var(--orange)}
.case-item p{font-size:4.6px;line-height:1.4;width:125px;color:#e8ecf5}
/* timeline */
.tl-frame{position:absolute;top:80px;width:112px;height:112px;border:1.5px solid var(--orange);padding:6px}
.tl-frame.dashed{border:1.5px dashed #fff}
.tl-box{width:100%;height:100%;background:#fff;border:3px solid var(--orange);display:flex;flex-direction:column;align-items:center;padding-top:10px;text-align:center}
.tl-box.filled{background:var(--orange);border-color:#fff}
.tl-box h6{font:700 6px "Montserrat",sans-serif;color:var(--orange);margin-top:6px}
.tl-box p{font-size:4.3px;line-height:1.35;color:var(--orange);padding:3px 8px}
.tl-box.filled h6,.tl-box.filled p{color:#fff}
/* team */
.team-band{position:absolute;left:0;right:0;top:142px;height:92px;background:#fff}
.member{position:absolute;top:118px;width:70px;text-align:center}
.avatar{width:50px;height:50px;margin:0 auto;border-radius:50%;border:3px solid var(--orange);background:linear-gradient(160deg,#f1e6dc,#c8b4a4)}
.member h6{font:700 6px "Montserrat",sans-serif;color:var(--orange);margin-top:3px}
.member p{font-size:4.6px;line-height:1.3;color:var(--ink)}
/* reframe */
.pill{position:absolute;top:52px;width:126px;height:34px;border-radius:18px;background:var(--silver);padding:4px}
.pill span{display:block;height:100%;border-radius:14px;background:#fff;font:700 9px/26px "Montserrat",sans-serif;color:var(--orange);text-align:center}
.reframe-col{position:absolute;top:110px;width:150px}
.reframe-col h6{font:400 6.5px "Lato",sans-serif;color:#fff;margin:0 0 2px}
.reframe-col h6::before{content:"▶ ";color:var(--orange);font-size:5px}
.reframe-col p{font-size:5px;line-height:1.3;color:#e8ecf5;margin:0 0 10px 12px}
/* options table */
.options{position:absolute;left:24px;top:46px;border-collapse:collapse;background:#fff;color:var(--ink);font:600 8px "Montserrat",sans-serif}
.options td,.options th{border:1px solid var(--navy);height:25px;padding:0 4px}
.options th{font:700 9.5px "Montserrat",sans-serif;color:var(--navy-deep);text-align:left;height:28px;padding-left:8px}
.options td:first-child{text-align:center;width:105px;font-size:8.5px;line-height:1.1}
.options td{width:74px}
.no{color:#e0203a;font-weight:400}
.ok{color:#1aa597}
.warn{color:#f4b400}
/* roadmap */
.step-label{position:absolute;top:159px;width:58px;height:14px;border-radius:2px;font:700 6px/14px "Montserrat",sans-serif;text-align:center;color:#fff;background:#2a2e36}
.step-label.light{background:#8e97ad}
.step-text{position:absolute;top:181px;width:70px;text-align:center;font-size:6.5px;line-height:1.3;color:#fff}
</style>
</head>
<body>

<!-- 1 cover -->
<section class="slide plain col-l r1">
  <div class="cover-card">
    <div class="cover-name"><i></i><span>Harbor Quill Industries</span></div>
    <div class="cover-thanks">THANK YOU</div>
  </div>
</section>

<!-- 2 agenda -->
<section class="slide col-r r1">
  <div style="position:absolute;left:31px;top:10px;width:21px;height:1.5px;background:#fff"></div>
  <div style="position:absolute;left:58px;top:10px;width:8px;height:1.5px;background:var(--orange)"></div>
  <div class="title" style="left:31px;top:20px;color:var(--orange);font-size:17px">Agenda</div>
  <p class="body" style="position:absolute;left:28px;top:57px;width:210px">Lorem ipsum dolor sit amet, consectetuer adipiscing elit. Maecenas porttitor congue massa. Fusce.</p>
  <div class="agenda-item" style="top:97px">1. WHO Harbor Quill Industries</div>
  <div class="agenda-item" style="top:132px">2. CERTIFICATIONS</div>
  <div class="agenda-item" style="top:162px">3. EDUCATION</div>
  <div class="agenda-item" style="top:192px">4. MEMBERSHIPS</div>
  <div class="photo" role="img" aria-label="Photo of a businessman in a suit holding a tablet" style="left:296px;top:68px;width:113px;height:145px;border-radius:16px;border-right:5px solid var(--orange);border-bottom:5px solid var(--orange);background:linear-gradient(160deg,#5a7fb5,#2a4a7a 60%,#1a2f50)"></div>
  <div class="brand-tag"><i></i><span>Harbor Quill Industries</span></div>
  <div class="footer-line"></div><div class="page-no">01</div>
</section>

<!-- 3 section divider -->
<section class="slide col-l r2">
  <div class="title" style="left:22px;top:12px">Section divider</div>
  <div class="brand-tag"><i></i><span>Harbor Quill Industries</span></div>
  <p class="body side-text" style="left:18px;top:68px">Lorem ipsum dolor sit amet, consectetuer adipiscing elit. Maecenas porttitor congue massa. Fusce posuere, magna sed pulvinar vctry</p>
  <p class="body side-text orange" style="left:302px;top:71px">Lorem ipsum dolor sit amet, consectetuer adipiscing elit. Maecenas porttitor congue massa. Fusce posuere, magna sed pulvinar vctry</p>
  <p class="body side-text orange" style="left:18px;top:173px">Lorem ipsum dolor sit amet, consectetuer adipiscing elit. Maecenas porttitor congue massa. Fusce posuere, magna sed pulvinar vctry</p>
  <p class="body side-text" style="left:302px;top:173px">Lorem ipsum dolor sit amet, consectetuer adipiscing elit. Maecenas porttitor congue massa. Fusce posuere, magna sed pulvinar vctry</p>
  <svg class="ring" style="left:160px;top:52px" width="150" height="150" viewBox="0 0 150 150">
    <circle cx="75" cy="75" r="57" fill="none" stroke="#e87722" stroke-width="2"/>
    <circle cx="75" cy="75" r="25" fill="#e87722"/>
    <g fill="#fff" stroke="#163a62" stroke-width="2">
      <circle cx="75" cy="18" r="15"/><circle cx="75" cy="132" r="15"/>
      <circle cx="18" cy="75" r="15" fill="#e87722"/><circle cx="132" cy="75" r="15" fill="#e87722"/>
    </g>
    <g fill="none" stroke="#163a62" stroke-width="1.6">
      <ellipse cx="75" cy="21" rx="7" ry="3"/><path d="M71 19 q4-9 8 0"/>
      <ellipse cx="75" cy="135" rx="7" ry="3"/><path d="M71 133 q4-9 8 0"/>
      <ellipse cx="18" cy="78" rx="7" ry="3"/><path d="M14 76 q4-9 8 0"/>
      <ellipse cx="132" cy="78" rx="7" ry="3"/><path d="M128 76 q4-9 8 0"/>
    </g>
  </svg>
  <div class="footer-line"></div><div class="page-no">02</div>
</section>

<!-- 4 about -->
<section class="slide col-r r2" style="left:610px">
  <div style="position:absolute;left:0;top:0;width:105px;height:175px;background:var(--navy)"></div>
  <div class="photo" role="img" aria-label="Photo of a presenter at a whiteboard with an audience member" style="left:28px;top:17px;width:170px;height:215px;border-radius:22px;border-right:6px solid var(--orange);border-bottom:6px solid var(--orange);background:linear-gradient(160deg,#f3f4f6,#d6d9de 55%,#8c7a6c)"></div>
  <div class="title" style="left:223px;top:19px;font-size:13px;text-decoration:underline">ABOUT <em>US</em></div>
  <div class="brand-tag"><i></i><span>Harbor Quill Industries</span></div>
  <p class="body" style="position:absolute;left:226px;top:62px;width:212px">Lorem ipsum dolor sit amet, consectetuer adipiscing elit. Maecenas porttitor congue massa. Fusce posuere, magna sed pulvinar ultricies, purus lectus malesuada libero, sit amet commodo magna eros quis urna.</p>
  <p class="body" style="position:absolute;left:226px;top:98px;width:212px">Lorem ipsum dolor sit amet, consectetuer adipiscing elit. Maecenas porttitor congue massa. Fusce posuere, magna sed pulvinar ultricies, purus lectus malesuada libero, sit amet commodo magna eros quis urna. Pellentesque habitant morbi tristique senectus et netus et malesuada fames ac turpis egestas. Proin pharetra nonummy pede. Mauris et orci. lectus malesuada libero, sit amet commodo magna eros quis urna. Pellentesque habitant morbi tristique senectus et netus et malesuada fames ac turpis egestas. Proin pharetra nonummy pede. Mauris et orci.</p>
  <div class="check-row" style="left:224px;top:179px"><b>✓</b><span>Lorem ipsum dolor sit amet, consectetuer adipiscing elit..</span></div>
  <div class="check-row" style="left:334px;top:179px"><b>✓</b><span>Lorem ipsum dolor sit amet, consectetuer adipiscing elit..</span></div>
  <div class="check-row" style="left:224px;top:209px"><b>✓</b><span>Lorem ipsum dolor sit amet, consectetuer adipiscing elit..</span></div>
  <div class="check-row" style="left:334px;top:209px"><b>✓</b><span>Lorem ipsum dolor sit amet, consectetuer adipiscing elit..</span></div>
  <div class="footer-line"></div><div class="page-no">03</div>
</section>

<!-- 5 the how -->
<section class="slide col-l r3">
  <div style="position:absolute;left:0;right:0;top:16px;text-align:center;font:700 11px 'Montserrat',sans-serif;text-decoration:underline">The How</div>
  <div style="position:absolute;left:0;right:0;top:47px;text-align:center;font:700 9.5px 'Montserrat',sans-serif">Harbor Quill Industries <span style="color:var(--orange)">services</span></div>
  <div class="brand-tag"><i></i><span>Harbor Quill Industries</span></div>
  <svg style="position:absolute;left:60px;top:86px" width="350" height="120" viewBox="0 0 350 120">
    <path d="M85 95 q40 50 85 0" fill="none" stroke="#e87722" stroke-width="2"/>
    <path d="M215 25 q40-45 85 0" fill="none" stroke="#e87722" stroke-width="2"/>
  </svg>
  <div class="how-circle" style="left:59px;top:93px">
    <svg width="22" height="22" viewBox="0 0 24 24" fill="none" stroke="#1d2b44" stroke-width="1.6"><path d="M6 10h12l-3-6H9z"/><path d="M12 10v11M8 21h8M4 8l2 1M20 8l-2 1M12 1v2"/></svg>
    <h4>Knowledge</h4><ul><li>Knowledge</li><li>Knowledge</li></ul>
  </div>
  <div class="how-circle" style="left:184px;top:89px;width:112px;height:112px;border:6px solid #8d96a8;box-shadow:inset 0 0 0 3px var(--orange)">
    <svg width="24" height="24" viewBox="0 0 24 24" fill="#e87722"><path d="M4 9h4a3 3 0 1 1 5 0h4v4a3 3 0 1 1 0 5v4h-4a3 3 0 1 0-5 0H4v-4a3 3 0 1 0 0-5z"/></svg>
    <h4>Knowledge</h4><ul><li>Knowledge</li><li>Knowledge</li></ul>
  </div>
  <div class="how-circle" style="left:318px;top:93px">
    <svg width="26" height="20" viewBox="0 0 26 20" fill="#1d2b44"><path d="M0 5l6-3 7 4 7-4 6 3-3 7-6 6-4-3-4 3-6-6z"/></svg>
    <h4>Knowledge</h4><ul><li>Knowledge</li><li>Knowledge</li></ul>
  </div>
  <div class="footer-line"></div><div class="page-no">04</div>
</section>

<!-- 6 charts -->
<section class="slide col-r r3" style="left:615px">
  <div class="title" style="left:32px;top:18px;font-size:12px">Charts &amp; <em style="margin-left:6px">data slide</em></div>
  <div class="brand-tag"><i></i><span>Harbor Quill Industries</span></div>
  <p class="body" style="position:absolute;left:20px;top:79px;width:188px;font-size:5px;line-height:1.42">Lorem ipsum dolor sit amet, consectetuer adipiscing elit, sed diam nonummy nibh euismod tincidunt ut laoreet dolore magna aliquam erat volutpat. Ut wisi enim ad minim veniam, quis Lorem ipsum dolor sit amet, consectetuer adipiscing elit, sed diam nonummy nibh euismod tincidunt ut laoreet dolore magna. Lorem ipsum dolor sit amet, consectetuer adipiscing elit, sed diam nonummy nibh euismod tincidunt ut laoreet dolore magna aliquam erat volutpat. Ut wisi enim ad minim veniam, quis Lorem ipsum dolor sit amet, consectetuer adipiscing elit, sed diam nonummy nibh euismod tincidunt ut laoreet dolore magna aliquam erat volutpat. Ut wisi enim ad minim veniam, quis Lorem ipsum dolor sit amet, consectetuer adipiscing elit, sed diam nonummy nibh euismod tincidunt ut laoreet dolore magna</p>
  <div style="position:absolute;left:312px;top:67px;font:700 7px 'Lato',sans-serif">Chart Title</div>
  <svg style="position:absolute;left:228px;top:84px" width="210" height="120" viewBox="0 0 210 120" aria-label="Bar chart with three series">
    <g stroke="rgba(255,255,255,.25)" stroke-width=".5">
      <line x1="22" y1="94" x2="180" y2="94"/><line x1="22" y1="76" x2="180" y2="76"/><line x1="22" y1="58" x2="180" y2="58"/><line x1="22" y1="40" x2="180" y2="40"/><line x1="22" y1="22" x2="180" y2="22"/>
    </g>
    <g fill="#3d6ccc">
      <rect x="26" y="50" width="10" height="44"/><rect x="66" y="64" width="10" height="30"/><rect x="104" y="58" width="10" height="36"/><rect x="142" y="40" width="10" height="54"/>
    </g>
    <g fill="#e87722">
      <rect x="40" y="62" width="8" height="32"/><rect x="80" y="30" width="8" height="64"/><rect x="118" y="70" width="8" height="24"/><rect x="156" y="58" width="8" height="36"/>
    </g>
    <g fill="#ffffff">
      <rect x="50" y="54" width="7" height="40"/><rect x="90" y="46" width="7" height="48"/><rect x="128" y="46" width="7" height="48"/><rect x="168" y="18" width="7" height="62"/>
    </g>
    <g fill="rgba(255,255,255,.4)" font-size="4" font-family="Lato">
      <text x="30" y="104">Category 1</text><text x="70" y="104">Category 2</text><text x="108" y="104">Category 3</text><text x="146" y="104">Category 4</text>
      <text x="78" y="116">■ Series 1 ■ Series 2 ■ Series 3</text>
    </g>
  </svg>
  <div class="footer-line"></div><div class="page-no">05</div>
</section>

<!-- 7 case study -->
<section class="slide col-l r4">
  <div class="title" style="left:29px;top:24px;font-size:12.5px">Case <em>Study</em></div>
  <div class="brand-tag"><i></i><span>Harbor Quill Industries</span></div>
  <div class="photo" role="img" aria-label="Close-up photo of a hand writing with a pen" style="left:41px;top:73px;width:126px;height:126px;border-radius:50%;border:3px solid var(--orange);background:radial-gradient(circle at 40% 35%,#f4e1d2,#d9b39a 50%,#b9bec8)"></div>
  <div class="case-item" style="top:54px"><div class="case-icon"><svg width="16" height="16" viewBox="0 0 24 24" fill="#e87722"><path d="M4 9h4a3 3 0 1 1 5 0h4v4a3 3 0 1 1 0 5v4h-4a3 3 0 1 0-5 0H4v-4a3 3 0 1 0 0-5z"/></svg></div><div><h5>Challenge</h5><p>nonummy nibh euismod tincidunt ut laoreet dolore magna aliquam erat volutpat. Ut wisi enim ad</p></div></div>
  <div class="case-item" style="top:117px"><div class="case-icon"><svg width="16" height="16" viewBox="0 0 24 24" fill="none" stroke="#e87722" stroke-width="1.6"><circle cx="12" cy="11" r="5"/><path d="M10 18h4M12 2v2M4 11H2M22 11h-2M5 4l1.5 1.5M19 4l-1.5 1.5"/></svg></div><div><h5>Solution</h5><p>nonummy nibh euismod tincidunt ut laoreet dolore magna aliquam erat volutpat. Ut wisi enim ad</p></div></div>
  <div class="case-item" style="top:180px"><div class="case-icon"><svg width="14" height="16" viewBox="0 0 20 24" fill="none" stroke="#e87722" stroke-width="1.6"><rect x="2" y="2" width="16" height="20" rx="1"/><path d="M6 8h8M6 12h8M6 16h8"/></svg></div><div><h5>Results</h5><p>nonummy nibh euismod tincidunt ut laoreet dolore magna aliquam erat volutpat. Ut wisi enim ad</p></div></div>
  <div class="footer-line"></div><div class="page-no">06</div>
</section>

<!-- 8 timeline -->
<section class="slide col-r r4" style="left:615px">
  <div class="title" style="left:42px;top:14px;font-size:15px">Timeline / <em>roadmap</em></div>
  <div class="brand-tag"><i></i><span>Harbor Quill Industries</span></div>
  <div class="tl-frame dashed" style="left:42px"><div class="tl-box">
    <svg width="28" height="22" viewBox="0 0 28 22" fill="#e87722"><ellipse cx="14" cy="17" rx="11" ry="4"/><path d="M8 14q2-10 6-13q0 6 4 6q1-3 2-4q2 5-1 11z"/></svg>
    <h6>Lorem ipsum</h6><p>Lorem ipsum dolor sit amet, consectetuer adipiscing elit, sed diam nonummy nibh euismod</p></div></div>
  <div class="tl-frame dashed" style="left:181px"><div class="tl-box filled">
    <svg width="24" height="24" viewBox="0 0 24 24" fill="none" stroke="#fff" stroke-width="1.6"><circle cx="12" cy="11" r="5"/><path d="M10 18h4M12 2v2M4 11H2M22 11h-2M5 4l1.5 1.5M19 4l-1.5 1.5"/></svg>
    <h6>Lorem ipsum</h6><p>Lorem ipsum dolor sit amet, consectetuer adipiscing elit, sed diam nonummy nibh euismod</p></div></div>
  <div class="tl-frame dashed" style="left:320px"><div class="tl-box">
    <svg width="22" height="22" viewBox="0 0 24 24" fill="#e87722"><path d="M4 9h4a3 3 0 1 1 5 0h4v4a3 3 0 1 1 0 5v4h-4a3 3 0 1 0-5 0H4v-4a3 3 0 1 0 0-5z"/></svg>
    <h6>Lorem ipsum</h6><p>Lorem ipsum dolor sit amet, consectetuer adipiscing elit, sed diam nonummy nibh euismod</p></div></div>
  <svg style="position:absolute;left:154px;top:132px" width="180" height="10" viewBox="0 0 180 10">
    <path d="M0 5h22" stroke="#fff" stroke-width="1"/><path d="M22 2l5 3-5 3z" fill="#fff"/>
    <path d="M139 5h22" stroke="#e87722" stroke-width="1"/><path d="M161 2l5 3-5 3z" fill="#e87722"/>
  </svg>
  <div class="footer-line"></div><div class="page-no">07</div>
</section>

<!-- 9 team -->
<section class="slide col-l r5">
  <div class="title" style="left:21px;top:11px;font-size:13px">TEAM <em>PROFILE</em></div>
  <div class="brand-tag"><i></i><span>Harbor Quill Industries</span></div>
  <p class="body" style="position:absolute;left:19px;top:37px;width:320px">Lorem ipsum dolor sit amet, consectetuer adipiscing elit. Maecenas porttitor congue massa. Fusce posuere, magna sed pulvinar ultricies, purus lectus malesuada libero, sit amet commodo magna eros quis urnaPellentesque habitant morbi tristique senectus et netus et malesuada fames ac turpis egestas. Proin pharetra nonummy pede. Mauris et orci.</p>
  <p class="body" style="position:absolute;left:19px;top:74px;width:320px">Lorem ipsum dolor sit amet, consectetuer adipiscing elit. Maecenas porttitor congue massa. Fusce posuere, magna sed pulvinar ultricies, purus lectus malesuada libero, sit amet commodo magna eros quis urnaPellentesque habitant morbi tristique senectus et netus et malesuada fames ac turpis egestas. Proin pharetra nonummy pede. Mauris et orci.</p>
  <div class="team-band"></div>
  <div class="member" style="left:29px"><div class="avatar" role="img" aria-label="Team member portrait"></div><h6>MEMBER NAME</h6><p>amet,consectetuer adipiscing elit, sed diamamet,consectetu er adipiscing elit, sed diam</p></div>
  <div class="member" style="left:114px"><div class="avatar" role="img" aria-label="Team member portrait"></div><h6>MEMBER NAME</h6><p>amet,consectetuer adipiscing elit, sed diamamet,consectetu er adipiscing elit, sed diam</p></div>
  <div class="member" style="left:199px"><div class="avatar" role="img" aria-label="Team member portrait"></div><h6>MEMBER NAME</h6><p>amet,consectetuer adipiscing elit, sed diamamet,consectetu er adipiscing elit, sed diam</p></div>
  <div class="member" style="left:285px"><div class="avatar" role="img" aria-label="Team member portrait"></div><h6>MEMBER NAME</h6><p>amet,consectetuer adipiscing elit, sed diamamet,consectetu er adipiscing elit, sed diam</p></div>
  <div class="member" style="left:368px"><div class="avatar" role="img" aria-label="Team member portrait"></div><h6>MEMBER NAME</h6><p>amet,consectetuer adipiscing elit, sed diamamet,consectetu er adipiscing elit, sed diam</p></div>
  <div class="footer-line"></div><div class="page-no">08</div>
</section>

<!-- 10 reframe -->
<section class="slide col-r r5" style="left:615px">
  <div class="title" style="left:26px;top:16px;font-size:15px">Reframe <em>Slide</em></div>
  <div class="brand-tag"><i></i><span>Harbor Quill Industries</span></div>
  <div style="position:absolute;left:58px;top:72px;width:356px;height:152px;border:1px dashed rgba(255,255,255,.45)"></div>
  <div style="position:absolute;left:233px;top:96px;width:1px;height:115px;background:rgba(255,255,255,.35)"></div>
  <div style="position:absolute;left:150px;top:68px;width:80px;height:1px;background:var(--orange)"></div>
  <div class="pill" style="left:80px"><span>PROBLEME</span></div>
  <div class="pill" style="left:258px"><span>SOLUTION</span></div>
  <div class="reframe-col" style="left:82px"><h6>Lorem ipsum</h6><p>Lorem ipsum dolor sit amet, consectetuer adipiscing elit. Maecenas porttitor congue massa. Maecenas porttitor congue massa.</p><h6>We prioritize</h6><p>Lorem ipsum dolor sit amet, consectetuer adipiscing elit. Maecenas porttitor congue massa. Maecenas porttitor congue massa.</p></div>
  <div class="reframe-col" style="left:261px"><h6>Lorem ipsum</h6><p>Lorem ipsum dolor sit amet, consectetuer adipiscing elit. Maecenas porttitor congue massa. Maecenas porttitor congue massa.</p><h6>We prioritize</h6><p>Lorem ipsum dolor sit amet, consectetuer adipiscing elit. Maecenas porttitor congue massa. Maecenas porttitor congue massa.</p></div>
  <div class="footer-line"></div><div class="page-no">09</div>
</section>

<!-- 11 options -->
<section class="slide col-l r6">
  <div class="title" style="left:17px;top:13px;font-size:16px">Options &amp; Trade - offs</div>
  <div class="brand-tag"><i></i><span>Harbor Quill Industries</span></div>
  <table class="options">
    <tr><th>Criterion</th><th>Option (A)</th><th>Option (B)</th><th>Option (C)</th></tr>
    <tr><td style="text-align:left;padding-left:16px">Cost</td><td>Expensive <span class="no">✗</span></td><td>Moderate <span class="warn">▲</span></td><td>Affordable <span class="ok">✓</span></td></tr>
    <tr><td>Implementation Time</td><td>Long &nbsp;&nbsp;<span class="no">✗</span></td><td>Medieum &nbsp;<span class="warn">▲</span></td><td>Short &nbsp;&nbsp;<span class="ok">✓</span></td></tr>
    <tr><td>ROI ( Return on Investment</td><td>Low &nbsp;&nbsp;&nbsp;<span class="no">✗</span></td><td>High <span class="ok">✓</span></td><td>Medieum <span class="warn">▲</span></td></tr>
    <tr><td style="font-size:10px">Complexity</td><td>High &nbsp;&nbsp;<span class="no">✗</span></td><td>Medieum <span class="warn">▲</span></td><td>Low &nbsp;&nbsp;&nbsp;<span class="ok">✓</span></td></tr>
    <tr><td style="font-size:10px">Risk Level</td><td>High &nbsp;&nbsp;<span class="no">✗</span></td><td>Low &nbsp;&nbsp;<span class="ok">✓</span></td><td>Medieum <span class="warn">▲</span></td></tr>
  </table>
  <div class="footer-line"></div><div class="page-no">10</div>
</section>

<!-- 12 execution roadmap -->
<section class="slide col-r r6" style="left:615px">
  <div class="title" style="left:61px;top:22px;font-size:13.5px">Execution Roadmap</div>
  <div class="brand-tag"><i></i><span>Harbor Quill Industries</span></div>
  <svg style="position:absolute;left:80px;top:62px" width="320" height="85" viewBox="0 0 320 85">
    <g fill="none" stroke-width="7">
      <path d="M6 40 a38 38 0 0 1 76 0" stroke="#e87722"/>
      <path d="M82 40 a38 38 0 0 0 76 0" stroke="#fff"/>
      <path d="M158 40 a38 38 0 0 1 76 0" stroke="#e87722"/>
      <path d="M234 40 a38 38 0 0 0 76 0" stroke="#fff"/>
    </g>
    <g fill="none" stroke="#fff" stroke-width="1.4">
      <circle cx="44" cy="34" r="6"/><path d="M41 43h6M44 22v3M34 34h-3M57 34h-3M37 27l1.5 1.5M51 27l-1.5 1.5"/>
      <path d="M110 30h6l2 3h12v10h-20z" fill="#fff"/>
      <path d="M185 34l8-5 6 4 6-4 8 5-5 6-5 4-4-3-4 3-5-4z" fill="#fff"/>
      <circle cx="268" cy="31" r="6"/><path d="M272 36l6 6"/>
    </g>
  </svg>
  <div class="step-label" style="left:89px">Lorem ipsum</div>
  <div class="step-label light" style="left:172px">Lorem ipsum</div>
  <div class="step-label" style="left:250px">Lorem ipsum</div>
  <div class="step-label light" style="left:332px">Lorem ipsum</div>
  <div class="step-text" style="left:83px">Lorem ipsum dolor sit aconsectetuer</div>
  <div class="step-text" style="left:166px">Lorem ipsum dolor sit aconsectetuer</div>
  <div class="step-text" style="left:244px">Lorem ipsum dolor sit aconsectetuer</div>
  <div class="step-text" style="left:326px">Lorem ipsum dolor sit aconsectetuer</div>
  <div class="footer-line"></div><div class="page-no">11</div>
</section>

<!-- 13 closing -->
<section class="slide plain r7" style="left:134px">
  <div class="cover-card">
    <div class="cover-name"><i></i><span>Harbor Quill Industries</span></div>
    <div class="cover-thanks">THANK YOU</div>
  </div>
</section>

</body>
</html>
```